Soulful musician needs contemporary cover art image for "Copperlane Hush" singles

"Copperlane Hush" singles are bluesy R&B songs, being offered as free downloads for Valentine's Day. We need a visual image that will brand these songs. Overall feel should be a contemporary take on vintage soul styles. Possible color palette might include dark reds, dark magentas, to suggest the Valentine's Day tie-in.
Attached are a crude concept sketch as well as previous cover images from this artist as style cues. Overall look and feel should be in similar territory to these past cover images. Please include title "Copperlane Hush" as well as artist name as shown in past examples. (NOTE: that's a shot glass in the concept sketch, although it's not required to use a shot glass or any other particular element).
Image should be square, at least 1400x1400 px at 300 dpi. Deliverable should include layered Photoshop and/or Illustrator source files, and identification of all fonts used.

```html
<!DOCTYPE html>
<html lang="en">
<head>
<meta charset="utf-8">
<title>Copperlane Hush — Single Cover</title>
<link href="https://fonts.googleapis.com/css2?family=Montserrat:wght@200;300&display=swap" rel="stylesheet">
<style>
  :root {
    --cover-plum: #530057;
    --shadow-plum: #3d0042;
    --type-pink: #f2a8f0;
    --glass-teal: #0eaec0;
    --glass-teal-deep: #0a919f;
    --heart-coral: #f74a4a;
  }
  html, body {
    margin: 0;
    padding: 0;
    width: 1200px;
    height: 1200px;
    overflow: hidden;
    background: var(--cover-plum);
  }
  .cover {
    position: relative;
    width: 1200px;
    height: 1200px;
    background: var(--cover-plum);
    font-family: "Montserrat", sans-serif;
    font-weight: 300;
    color: var(--type-pink);
  }
  .artist-name,
  .single-title {
    position: absolute;
    left: 0;
    width: 1200px;
    margin: 0;
    text-align: center;
    text-transform: uppercase;
    font-weight: 300;
    line-height: 1;
    white-space: nowrap;
    box-sizing: border-box;
  }
  .artist-name {
    top: 109px;
    font-size: 46px;
    letter-spacing: 0.22em;
    padding-left: 0.22em;
  }
  .single-title {
    top: 1055px;
    font-size: 45px;
    letter-spacing: 0.56em;
    padding-left: 0.56em;
    transform: translateX(-20px);
  }
  .artwork {
    position: absolute;
    left: 0;
    top: 0;
    width: 1200px;
    height: 1200px;
  }
</style>
</head>
<body>
  <main class="cover">
    <h2 class="artist-name">The Soul of Marlow Reed</h2>

    <svg class="artwork" viewBox="0 0 1200 1200" width="1200" height="1200">
      <defs>
        <radialGradient id="hero-tones" cx="0.5" cy="0.45" r="0.62">
          <stop offset="0" stop-color="var(--heart-coral)"/>
          <stop offset="0.32" stop-color="var(--heart-coral)" stop-opacity="0.85"/>
          <stop offset="0.55" stop-color="var(--glass-teal)"/>
          <stop offset="0.85" stop-color="var(--glass-teal-deep)"/>
          <stop offset="1" stop-color="var(--shadow-plum)"/>
        </radialGradient>
      </defs>
      <rect class="hero-illustration"
            x="369" y="370" width="415" height="431" rx="24"
            fill="url(#hero-tones)"
            role="img"
            aria-label="Illustration of a teal shot glass with a red Valentine heart on it, casting a dark oval shadow"/>
    </svg>

    <h1 class="single-title">Copperlane Hush</h1>
  </main>
</body>
</html>
```